Water Bottle Design

We are launching a water bottle and need a impactful design.

Target Market(s)

health conscious hipsters

Font styles to use
Sans Serif

Requirements
Must have
• Please include the logo (included) on one side of the bottle and these words on the other side of the bottle. "It’s simple, REUSE this bottle every day. Your action, will REDUCE the amount of waste produced. SAVE your body from drinking the harmful contaminants in your water from Non-BPA plastics. HELP someone else because proceeds from your purchase will help homeless veterans.
• We’re just two dudes that like to drink water and help people. #PayItFoward"
• Use a total of two colors
• UPDATE: You do not have to use the bottle on the logo.
Nice to have
• The bottle itself is 34 ounces and looks like a normal water bottle. I will include the image in the files. We would need to be able to change the colors easily.
Should not have
• Do not use more than two colors. Colors should not be important to the design at this point.

```html
<!DOCTYPE html>
<html lang="en">
<head>
<meta charset="utf-8">
<title>GIB Water Bottle – Two Sides</title>
<link href="https://fonts.googleapis.com/css2?family=Raleway:wght@300;400&display=swap" rel="stylesheet">
<style>
  :root {
    --bg: #ffffff;
    --sky-top: #c9edf6;
    --sky-bottom: #7fd3e8;
    --sea-top: #4cc6dc;
    --sea-bottom: #20a9c4;
    --ink: #1f9ccb;
    --text-light: #ffffff;
    --steel-light: #e4e6e8;
    --steel-mid: #b9bdc1;
    --steel-dark: #8c9196;
  }
  html, body {
    margin: 0;
    padding: 0;
    overflow: hidden;
    background: var(--bg);
  }
  .canvas {
    position: relative;
    width: 1200px;
    height: 1192px;
    overflow: hidden;
    background: var(--bg);
    font-family: "Raleway", "Helvetica Neue", Arial, sans-serif;
  }
  .bottles {
    position: absolute;
    inset: 0;
  }
  .brand {
    position: absolute;
    left: 770px;
    top: 360px;
    width: 150px;
    text-align: left;
    color: var(--ink);
    font-weight: 300;
  }
  .brand-name {
    display: block;
    font-size: 84px;
    line-height: 1;
    letter-spacing: 2px;
  }
  .brand-tagline {
    display: block;
    margin-top: 6px;
    font-size: 17px;
    line-height: 1;
  }
  .message {
    position: absolute;
    left: 730px;
    top: 518px;
    width: 226px;
    margin: 0;
    text-align: center;
    font-size: 10px;
    font-weight: 400;
    line-height: 47px;
  }
  .message .above-water { color: var(--ink); }
  .message .below-water { color: var(--text-light); }
</style>
</head>
<body>
<div class="canvas">
  <svg class="bottles" width="1200" height="1192" viewBox="0 0 1200 1192">
    <defs>
      <linearGradient id="skyFill" x1="0" y1="0" x2="0" y2="1">
        <stop offset="0" stop-color="var(--sky-top)"/>
        <stop offset="1" stop-color="var(--sky-bottom)"/>
      </linearGradient>
      <linearGradient id="seaFill" x1="0" y1="0" x2="0" y2="1">
        <stop offset="0" stop-color="var(--sea-top)"/>
        <stop offset="1" stop-color="var(--sea-bottom)"/>
      </linearGradient>
      <linearGradient id="steelFill" x1="0" y1="0" x2="1" y2="0">
        <stop offset="0" stop-color="var(--steel-dark)"/>
        <stop offset="0.35" stop-color="var(--steel-light)"/>
        <stop offset="0.7" stop-color="var(--steel-mid)"/>
        <stop offset="1" stop-color="var(--steel-dark)"/>
      </linearGradient>
      <clipPath id="bottleShape">
        <path d="M318 142 L402 142 C405 230 488 280 488 360 L488 960 Q488 990 460 990 L260 990 Q232 990 232 960 L232 360 C232 280 315 230 318 142 Z"/>
      </clipPath>
    </defs>

    <!-- Front side: ocean scene wrap -->
    <g class="bottle bottle-front">
      <g clip-path="url(#bottleShape)">
        <rect class="wrap-sky" x="232" y="142" width="256" height="560" fill="url(#skyFill)"/>
        <rect class="wrap-scene" x="232" y="142" width="256" height="782" fill="url(#skyFill)" opacity="0"
              role="img" aria-label="Illustration: a diver plunging into the ocean, with a small fish and a jellyfish below the waves"/>
        <path class="wrap-sea" d="M232 700 Q272 684 312 698 T392 696 T488 694 L488 924 L232 924 Z" fill="url(#seaFill)"/>
        <rect class="steel-base" x="232" y="924" width="256" height="70" fill="url(#steelFill)"/>
      </g>
      <g class="cap">
        <rect x="300" y="52" width="128" height="90" rx="8" fill="url(#steelFill)"/>
        <rect x="300" y="60" width="128" height="30" fill="url(#steelFill)" opacity="0.7"/>
      </g>
    </g>

    <!-- Back side: logo and message wrap -->
    <g class="bottle bottle-back" transform="translate(483 0)">
      <g clip-path="url(#bottleShape)">
        <rect class="wrap-sky" x="232" y="142" width="256" height="560" fill="url(#skyFill)"/>
        <path class="wrap-sea" d="M232 690 Q272 676 312 688 T392 686 T488 684 L488 924 L232 924 Z" fill="url(#seaFill)"
              role="img" aria-label="Illustration: ocean waves with seaweed along the bottom"/>
        <rect class="steel-base" x="232" y="924" width="256" height="70" fill="url(#steelFill)"/>
      </g>
      <g class="cap">
        <rect x="300" y="52" width="128" height="90" rx="8" fill="url(#steelFill)"/>
        <rect x="300" y="60" width="128" height="30" fill="url(#steelFill)" opacity="0.7"/>
      </g>
    </g>
  </svg>

  <div class="brand">
    <span class="brand-name">GIB</span>
    <span class="brand-tagline">Give It Back</span>
  </div>

  <p class="message">
    <span class="above-water">"It's simple, REUSE this bottle every<br>
    day. Your action, will REDUCE the<br>
    amount of waste produced. SAVE<br>
    your body from drinking the harmful</span><br>
    <span class="below-water">contaminants in your water from<br>
    Non-BPA plastics. HELP someone<br>
    else because proceeds from your<br>
    purchase will help homeless veterans.</span>
  </p>
</div>
</body>
</html>
```